Finish My Wordpress Site for Local Painting Company

The site is almost done, but I'm stuck and need expert assistance. Would love to work with someone over zoom so that I can express what I've been trying to accomplish and to learn more about the back end of Wordpress. Here's what's left to be done (I think):

Upload New Photos
Gallery (Before&After)
Anchors to: Get a Quote, Gallery
Font consistency
More padding at the bottom of pages?
Edit padding on Contact page?
Links (photos, buttons, social), add domains, edit page names
Normal entrance animation?
Mobile version

And here's the site as is:
http://qv7.b19.zentrivault.example/

Coding

Coded - Design and coding required

Number of Pages Required

1 page

Colors
0355a3

Requirements
Must have
• Communication between us as the work gets done

```html
<!DOCTYPE html>
<html lang="en">
<head>
<meta charset="utf-8">
<title>Maple Lane Painting</title>
<link rel="stylesheet" href="https://fonts.googleapis.com/css2?family=Poppins:wght@400;500;600&family=Montserrat:wght@600;700&family=Bree+Serif&display=swap">
<style>
:root{
  --blue:#0b62ad;
  --blue-dark:#0355a3;
  --tan:#9d8878;
  --tan-light:#a8907c;
  --white:#ffffff;
  --card-text:#0b62ad;
  --input:#f4f4f4;
}
*{box-sizing:border-box;margin:0;padding:0}
html,body{width:1200px;height:3063px;overflow:hidden}
body{position:relative;background:var(--tan);font-family:"Poppins",sans-serif;color:var(--white)}
.abs{position:absolute}
.center{left:0;width:1200px;text-align:center}

/* hero */
.hero{top:0;left:0;width:1200px;height:666px;
  background:linear-gradient(180deg,#b07a45 0%,#c89a66 12%,rgba(0,0,0,0) 30%),
  linear-gradient(90deg,#6f8a95 0%,#7a9a7e 25%,#8a6b4e 45%,#c9b49a 65%,#b8a48c 85%,#a48f73 100%);}
.hero-title{top:296px;font-family:"Montserrat",sans-serif;font-weight:700;font-size:35px;text-shadow:0 2px 6px rgba(0,0,0,.5)}
.hero-sub{top:348px;font-size:13px;font-weight:500;text-shadow:0 1px 4px rgba(0,0,0,.6)}

/* top bar */
.topbar{top:666px;left:0;width:1200px;height:76px;background:var(--blue)}
.topbar-contact{left:277px;width:200px;top:19px;text-align:center;font-size:11px;line-height:21px}
.brand{display:flex;align-items:center;gap:8px}
.brand-dot{width:34px;height:34px;border-radius:50%;border:2px solid var(--white)}
.brand-name{font-family:"Poppins",sans-serif;font-weight:600;font-size:13px;color:var(--white)}
.topbar .brand{left:540px;top:21px}
.nav{left:700px;top:22px;display:grid;grid-template-columns:60px 60px 60px;row-gap:4px;font-size:11px;text-align:center;line-height:14px}

/* copy */
.copy{left:295px;width:610px;text-align:center;font-size:10px;line-height:15px}
.brush{left:585px;width:30px;height:30px}

/* circles */
.circle{width:216px;height:216px;border-radius:50%;border:3px solid var(--blue);display:flex;align-items:center;justify-content:center;text-align:center;
  font-family:"Montserrat",sans-serif;font-weight:700;font-size:19px;line-height:23px;padding:0 14px;text-shadow:0 2px 4px rgba(0,0,0,.55)}
.c-cabinets{background:linear-gradient(90deg,#3b7fbd 0%,#d9dde2 35%,#f2f2f2 55%,#8f959c 100%)}
.c-quote{background:linear-gradient(110deg,#7a6a4c 0%,#d8d2c2 40%,#e6e2d8 60%,#8c7552 100%)}
.c-reviews{background:linear-gradient(180deg,#4f7a34 0%,#6b9a3e 55%,#c7d3df 80%,#8aa6c6 100%)}
.c-crew{background:linear-gradient(160deg,#6a6f74 0%,#b6bcc2 50%,#8c8f92 100%)}
.c-guarantee{background:linear-gradient(180deg,#c6c7bd 0%,#8fae55 45%,#e07a2a 65%,#5f8d3a 100%)}
.c-talk{background:linear-gradient(160deg,#5c6168 0%,#c9ccd0 45%,#9aa0a6 100%)}

/* wood band */
.wood{top:1397px;left:0;width:1200px;height:171px;
  background:linear-gradient(90deg,#5d6166 0%,#7a4a2c 8%,#a0603a 25%,#8a5331 45%,#a86a42 65%,#8d5634 85%,#6b8a4a 100%)}
.svc{width:220px;text-align:center;font-family:"Montserrat",sans-serif;font-weight:700;font-size:17px;line-height:30px;text-shadow:0 2px 4px rgba(0,0,0,.6)}

.tagline{top:1610px;font-size:13px;font-weight:500}

/* reviews */
.card{top:2047px;width:294px;height:103px;background:var(--white);border:2px solid var(--blue);padding:10px 10px;color:var(--card-text)}
.card-head{display:flex;align-items:center;gap:8px}
.avatar{width:20px;height:20px;border-radius:50%;background:#d5dbe2}
.card-name{font-family:"Bree Serif",serif;font-size:10px;line-height:11px}
.stars{font-size:9px;letter-spacing:1px;line-height:10px}
.card-text{margin-top:8px;font-family:"Poppins",sans-serif;font-weight:500;font-size:8.6px;line-height:12.5px}
.arrow{top:2087px;font-size:16px;color:var(--white)}
.dots{top:2160px;left:553px;display:flex;gap:8px}
.dots span{width:4px;height:4px;border-radius:50%;background:#6f5f52}
.dots span.on{background:#111}

.h2{font-family:"Poppins",sans-serif;font-weight:600;font-size:19px}
.socials{display:flex;gap:4px}
.socials span{width:26px;height:26px;border-radius:50%;background:var(--blue)}
.footer .socials span{background:var(--tan-light)}

/* newsletter */
.nl-input{top:2425px;left:454px;width:191px;height:28px;background:var(--input);border:1px solid #ddd;color:#7a8fb0;font-size:9px;padding:9px 8px}
.nl-btn{top:2425px;left:650px;width:96px;height:28px;background:var(--blue);font-size:9px;font-weight:600;text-align:center;line-height:28px}

/* quote */
.quote-bg{top:2502px;left:0;width:1200px;height:337px;background:linear-gradient(90deg,#b08a4c 0%,#d9b87a 10%,#6d5a3a 17%,#6d5a3a 83%,#3f5a2e 88%,#4a6a35 100%)}
.quote-box{top:2502px;left:200px;width:851px;height:337px;background:linear-gradient(180deg,#b9c4cf 0%,#9fb0c2 35%,#2f73b5 75%,var(--blue) 100%)}
.quote-title{top:2530px;font-family:"Montserrat",sans-serif;font-weight:700;font-size:23px;text-shadow:0 2px 4px rgba(0,0,0,.35)}
.quote-sub{top:2576px;font-size:11px}
.q-contact{width:260px;text-align:center;font-size:16px}
.field{left:608px;width:248px;background:var(--input);border:1px solid #ccc;color:#7a8fb0;font-size:9px;padding:8px 8px}
.send{top:2777px;left:608px;width:248px;height:28px;background:var(--tan);font-size:10px;text-align:center;line-height:28px}

/* footer */
.footer{top:2839px;left:0;width:1200px;height:224px;background:var(--blue)}
.foot-name{left:247px;top:40px;font-family:"Bree Serif",serif;font-size:24px;line-height:26px}
.foot-area{left:247px;top:106px;width:240px;font-family:"Bree Serif",serif;font-size:8.5px;line-height:17px}
.footer .socials{left:247px;top:166px}
.footer .brand{left:552px;top:58px;flex-direction:column;gap:4px}
.footer .brand-dot{width:60px;height:60px}
.est{left:560px;top:150px;width:88px;text-align:center;font-size:9px;font-weight:600}
.info{font-size:9.5px;line-height:13px}
.ico{width:18px;height:18px}
</style>
</head>
<body>

<section class="abs hero" role="img" aria-label="Bright bedroom with wood ceiling and glass wall opening to a mountain view"></section>
<h1 class="abs center hero-title">Maple Lane Painting</h1>
<p class="abs center hero-sub">Where preparation makes all the difference.</p>

<header class="abs topbar">
  <div class="abs topbar-contact">(555) 014-2287<br>glen@maplelanepaint.example</div>
  <div class="abs brand"><span class="brand-dot"></span><span class="brand-name">Maple Lane</span></div>
  <nav class="abs nav"><span>Services</span><span>Gallery</span><span>Reviews</span><span>About</span><span>Blog</span><span>Contact</span></nav>
</header>

<p class="abs copy" style="top:803px">At Maple Lane's, we offer an array of paint services in the Cambridge, Waltham, and Metrowest areas. Our preparation is unparalleled, and we use nothing short of the best methods so that you can sit down and relax with a glass of lemonade, knowing that all your concerns are going to be taken care of by an expert painter you can trust.</p>

<svg class="abs brush" style="top:880px" viewBox="0 0 30 30" aria-hidden="true"><g fill="#fff"><rect x="13" y="2" width="8" height="15" rx="3" transform="rotate(40 17 10)"/><path d="M9 18c3-1 5 1 5 4 0 4-5 6-10 6 2-2 1-9 5-10z"/></g></svg>

<div class="abs circle c-cabinets" style="left:252px;top:959px" role="img" aria-label="Painter brushing white cabinet trim">Kitchen Cabinets</div>
<div class="abs circle c-quote" style="left:492px;top:959px" role="img" aria-label="Quote sheet on a clipboard">Get A Quote</div>
<div class="abs circle c-reviews" style="left:731px;top:959px" role="img" aria-label="Paint can with brush among green shrubs">See What Our Customers have to Say</div>

<p class="abs copy" style="top:1232px">We have reliable systems that help us to avoid mistakes, address every concern, and ensure your job runs seamlessly. We are lead safe certified and use environmentally friendly, zero VOC products to complete all our projects. Our crisp lines, attention to detail, personalized customer service, and competitive rates make Maple Lane's the most unrivaled painting company you will find in the area and the best choice for all your painting needs.</p>

<svg class="abs brush" style="top:1330px" viewBox="0 0 30 30" aria-hidden="true"><g fill="#fff"><rect x="13" y="2" width="8" height="15" rx="3" transform="rotate(40 17 10)"/><path d="M9 18c3-1 5 1 5 4 0 4-5 6-10 6 2-2 1-9 5-10z"/></g></svg>

<section class="abs wood" role="img" aria-label="Stained wooden fence boards with a potted plant">
  <div class="abs svc" style="left:260px;top:34px">Interior<br>Pressure Wash<br>Kitchen Cabinets</div>
  <div class="abs svc" style="left:484px;top:35px">Exterior<br>Commercial<br>Graffiti Removal</div>
  <div class="abs svc" style="left:720px;top:34px">Carpentry<br>EMF Shielding<br>Faux &amp; Decorative</div>
</section>

<p class="abs center tagline">No matter the job, Maple Lane's will make it happen.</p>

<svg class="abs brush" style="top:1664px" viewBox="0 0 30 30" aria-hidden="true"><g fill="#fff"><rect x="13" y="2" width="8" height="15" rx="3" transform="rotate(40 17 10)"/><path d="M9 18c3-1 5 1 5 4 0 4-5 6-10 6 2-2 1-9 5-10z"/></g></svg>

<div class="abs circle c-crew" style="left:252px;top:1747px" role="img" aria-label="Ladder and paint bucket against house siding">Painters &amp; Carpenters You can Trust</div>
<div class="abs circle c-guarantee" style="left:492px;top:1747px" role="img" aria-label="Orange tulips in a front yard">100% Satisfaction Guaranteed</div>
<div class="abs circle c-talk" style="left:731px;top:1747px" role="img" aria-label="Freshly painted house entrance">Let's Talk Painting</div>

<span class="abs arrow" style="left:287px">&#8249;</span>
<article class="abs card" style="left:302px">
  <div class="card-head"><span class="avatar"></span><div><div class="card-name">Paula R.</div><div class="stars">★★★★★</div></div></div>
  <p class="card-text">The team was courteous and careful, showed up on time and with appropriate scheduling and notification. Most importantly, the team did a fantastic job, well above and beyond my expectations.</p>
</article>
<article class="abs card" style="left:606px">
  <div class="card-head"><span class="avatar"></span><div><div class="card-name">Ken M.</div><div class="stars">★★★★★</div></div></div>
  <p class="card-text">We have worked with Glen for many years. His work is first rate. A professional crew that leaves the site in pristine shape. A pleasure to work with them on both interior and exterior projects!</p>
</article>
<span class="abs arrow" style="left:905px">&#8250;</span>
<div class="abs dots"><span></span><span></span><span></span><span></span><span></span><span></span><span></span><span></span><span class="on"></span></div>

<h2 class="abs center h2" style="top:2226px">Follow, Like &amp; Leaves us a review</h2>
<div class="abs socials" style="left:526px;top:2269px"><span></span><span></span><span></span><span></span><span></span></div>

<svg class="abs brush" style="top:2323px" viewBox="0 0 30 30" aria-hidden="true"><g fill="#fff"><rect x="13" y="2" width="8" height="15" rx="3" transform="rotate(40 17 10)"/><path d="M9 18c3-1 5 1 5 4 0 4-5 6-10 6 2-2 1-9 5-10z"/></g></svg>

<h2 class="abs center h2" style="top:2378px">Subbscribe to Our Newsletter</h2>
<div class="abs nl-input">Email</div>
<div class="abs nl-btn">Subscribe</div>

<section class="abs quote-bg" role="img" aria-label="Wooden lattice and grass behind a job estimate sheet"></section>
<section class="abs quote-box" role="img" aria-label="Job details estimate sheet fading into blue"></section>
<h2 class="abs center quote-title">Get A Quote</h2>
<p class="abs center quote-sub">Call, email us, or just fill out the form and we'll get back to you right away.</p>
<svg class="abs ico" style="left:421px;top:2636px" viewBox="0 0 24 24" aria-hidden="true"><path fill="#c9b79a" d="M6.6 10.8a15 15 0 0 0 6.6 6.6l2.2-2.2c.3-.3.7-.4 1-.2 1.1.4 2.3.6 3.6.6.6 0 1 .4 1 1V20c0 .6-.4 1-1 1C10.6 21 3 13.4 3 4c0-.6.4-1 1-1h3.5c.6 0 1 .4 1 1 0 1.3.2 2.5.6 3.6.1.3 0 .7-.2 1z"/></svg>
<div class="abs q-contact" style="left:300px;top:2661px">(555) 014-2287</div>
<svg class="abs ico" style="left:413px;top:2723px" viewBox="0 0 24 24" aria-hidden="true"><path fill="#c9b79a" d="M2 5h20v14H2z"/><path fill="none" stroke="#8aa6c6" stroke-width="1.6" d="M2 5l10 8 10-8"/></svg>
<div class="abs q-contact" style="left:270px;top:2759px;width:320px">glen@maplelanepaint.example</div>
<div class="abs field" style="top:2619px;height:30px">Name</div>
<div class="abs field" style="top:2657px;height:30px">Email</div>
<div class="abs field" style="top:2696px;height:75px">Message</div>
<div class="abs send">Send</div>

<footer class="abs footer">
  <div class="abs foot-name">Maple Lane<br>Painting©</div>
  <p class="abs foot-area">Serving Cambridge, Waltham, Arlington, Lincoln, Belmont, Newton, Watertown, Weston, Dover, Winchester, Medford, and Lexington areas.</p>
  <div class="abs socials"><span></span><span></span><span></span><span></span><span></span></div>
  <div class="abs brand"><span class="brand-dot"></span><span class="brand-name">Maple Lane</span></div>
  <div class="abs est">Est. 1985</div>

  <div class="abs info" style="left:660px;top:30px;width:156px;text-align:right">Mon-Fri: 7am-7pm</div>
  <svg class="abs ico" style="left:796px;top:28px" viewBox="0 0 24 24" aria-hidden="true"><circle cx="12" cy="12" r="10" fill="#b8c6d6"/><path d="M12 6v6l4 2" stroke="#0b62ad" stroke-width="2" fill="none"/></svg>
  <div class="abs info" style="left:660px;top:67px;width:124px;text-align:right">(555) 014-2287</div>
  <svg class="abs ico" style="left:796px;top:64px" viewBox="0 0 24 24" aria-hidden="true"><path fill="#b8c6d6" d="M6.6 10.8a15 15 0 0 0 6.6 6.6l2.2-2.2c.3-.3.7-.4 1-.2 1.1.4 2.3.6 3.6.6.6 0 1 .4 1 1V20c0 .6-.4 1-1 1C10.6 21 3 13.4 3 4c0-.6.4-1 1-1h3.5c.6 0 1 .4 1 1 0 1.3.2 2.5.6 3.6.1.3 0 .7-.2 1z"/></svg>
  <div class="abs info" style="left:600px;top:105px;width:184px;text-align:right;font-size:9px">glen@maplelanepaint.example</div>
  <svg class="abs ico" style="left:796px;top:102px" viewBox="0 0 24 24" aria-hidden="true"><path fill="#b8c6d6" d="M2 5h20v14H2z"/><path fill="none" stroke="#0b62ad" stroke-width="1.6" d="M2 5l10 8 10-8"/></svg>

  <div class="abs info" style="left:848px;top:30px;width:110px;text-align:center">48 Orchard Row, 2B,<br>Cambridge, MA 02139</div>
  <svg class="abs ico" style="left:962px;top:30px;width:22px" viewBox="0 0 24 24" aria-hidden="true"><rect x="2" y="5" width="20" height="14" rx="2" fill="none" stroke="#b8c6d6" stroke-width="1.6"/><circle cx="8" cy="11" r="2" fill="#b8c6d6"/><path d="M13 10h6M13 14h6" stroke="#b8c6d6" stroke-width="1.4"/></svg>
  <div class="abs info" style="left:840px;top:90px;width:120px;text-align:center">112 Cedar Street, #7,<br>Waltham, MA 02451</div>
</footer>

</body>
</html>
```